Dental Office Needs- Flyer Design for Same Day Crowns

We need a flyer that will explain the benefits of the same day crown from the patient prospective. Not show pictures of the machine that makes the crowns. See attached material for content. The flyer should use the practices PMS colors of Green 562 and Blue 3025. The ad should say to the patient - I want to go this office and get my crown done there.
Updates

Project Deadline Extended Reason: The difference in the time zone between USA and Europe has caused issues. Minor changes still need to be worked out. Added Thursday, July 14, 2016

Target Market(s)

Dental Patients

Industry/Entity Type

Dental

Requirements
Must have
• Call to Action
• Business Address and Business Logo
• Classic Design
• images of a Happy 50 year old Couple
• Gives the benefits of the same day crown
Should not have
• No Images of tooth figures
• No before or after pictures

```html
<!DOCTYPE html>
<html lang="en">
<head>
<meta charset="utf-8">
<title>Oakridge Dental Care – Same-Day Crowns Flyer</title>
<link rel="stylesheet" href="https://fonts.googleapis.com/css2?family=Arimo:wght@400;700&display=swap">
<style>
:root{
  --page-bg:#3a3a3a;
  --paper:#ffffff;
  --ink:#1a1a1a;
  --brand-blue:#1c4f7c;
  --brand-teal:#0f6f7a;
  --alert-red:#e2131a;
  --green-light:#2db36a;
  --green-mid:#129a4d;
  --green-deep:#0c9244;
  --band-green:#30b56b;
  --lime:#8cbf26;
  --violet:#662d8c;
  --magenta:#d4145a;
  --photo-leaf:#a9c46a;
  --photo-sun:#eef0c8;
  --photo-bloom:#7d78c4;
}
*{box-sizing:border-box;margin:0;padding:0}
html,body{width:1200px;height:1200px;overflow:hidden;background:var(--page-bg)}
body{font-family:"Arimo",Arial,sans-serif;color:var(--ink);position:relative}
.flyer{
  position:absolute;left:159px;top:30px;width:1050px;height:1358px;
  background:var(--paper);transform:scale(0.8395);transform-origin:0 0;
  box-shadow:0 10px 30px rgba(0,0,0,.5);
}
.flyer > *{position:absolute}
.hero-photo{
  left:31px;top:28px;width:986px;height:657px;
  background:
    radial-gradient(ellipse 45% 55% at 72% 45%, #f3e4d0 0%, rgba(243,228,208,0) 70%),
    radial-gradient(ellipse 60% 35% at 50% 95%, var(--photo-bloom) 0%, rgba(125,120,196,0) 75%),
    linear-gradient(180deg,var(--photo-sun) 0%,var(--photo-leaf) 55%,#6f9a3e 100%);
}
.site-url{left:101px;top:94px;font-size:18px;letter-spacing:2.6px;color:#222}
.call-box{
  left:135px;top:160px;width:280px;height:76px;border:1.5px solid #333;border-radius:8px;
  text-align:center;
}
.call-box .label{
  position:absolute;left:50%;top:-16px;transform:translateX(-50%);
  padding:0 12px;background:#f1f2cf;font-size:28px;color:#111;line-height:30px;
}
.call-box .phone{display:block;margin-top:24px;font-size:40px;font-weight:700;color:var(--alert-red);line-height:44px}
.promo-badge{
  left:105px;top:280px;width:340px;height:240px;background:var(--alert-red);
  border:8px solid #fff;transform:rotate(-4deg);
  display:flex;align-items:center;justify-content:center;text-align:center;
  color:#fff;font-weight:700;font-size:50px;line-height:62px;
  box-shadow:0 4px 10px rgba(0,0,0,.25);
}
.brand-card{
  left:71px;top:588px;width:421px;height:200px;background:#fff;
  box-shadow:0 3px 8px rgba(0,0,0,.3);text-align:center;
  display:flex;flex-direction:column;justify-content:center;align-items:center;gap:14px;
}
.brand-name{font-size:38px;color:var(--brand-blue);font-weight:400}
.brand-tagline{font-size:20px;color:var(--brand-teal)}
.intro-heading{
  left:60px;top:806px;width:444px;text-align:center;
  font-size:26px;line-height:31.5px;color:var(--brand-blue);text-transform:uppercase;
}
.benefit{
  left:170px;width:223px;height:68px;border-radius:4px;color:#fff;
  font-size:19px;line-height:24px;display:flex;align-items:center;justify-content:center;text-align:center;
}
.benefit--sameday{top:947px;background:var(--lime)}
.benefit--fit{top:1036px;background:var(--alert-red)}
.benefit--look{top:1124px;background:var(--violet)}
.benefit--relax{top:1213px;background:var(--magenta)}
.plus{left:264px;width:34px;height:34px}
.goodbye{left:588px;width:429px;color:#fff;padding-left:21px;font-size:52px;line-height:62px;border-radius:8px}
.goodbye--crown{top:679px;height:200px;background:var(--green-light);padding-top:10px;border-bottom:2px solid #fff}
.goodbye--visit{top:878px;height:150px;background:var(--green-mid);padding-top:14px;border-radius:0 0 8px 8px;border-bottom:2px solid #fff}
.goodbye--tray{top:1027px;height:125px;background:var(--green-deep);font-weight:400;letter-spacing:-1px;padding-top:2px;opacity:.97;-webkit-text-stroke:0;font-size:54px}
.goodbye--tray span{font-weight:400;color:#eafff1}
.details{left:588px;top:1169px;width:429px;font-size:15.5px;line-height:20.5px;text-align:justify;color:#111}
.details p + p{margin-top:20px}
.contact-band{
  left:0;top:1302px;width:1050px;height:56px;background:var(--band-green);
  color:#fff;font-size:19.5px;display:flex;align-items:center;justify-content:center;gap:14px;
}
</style>
</head>
<body>
<div class="flyer">
  <div class="hero-photo" role="img" aria-label="Smiling older couple sitting among bluebells in a sunlit spring forest"></div>
  <div class="site-url">www.oakridgedentalcare.com</div>
  <div class="call-box"><span class="label">CALL</span><span class="phone">555.014.0372</span></div>
  <div class="promo-badge">2 HOURS<br>INSTEAD OF<br>2 VISITS.</div>

  <div class="brand-card">
    <div class="brand-name">Oakridge Dental Care</div>
    <div class="brand-tagline">It All Begins With a Healthy Smile!</div>
  </div>

  <h1 class="intro-heading" style="font-weight:400">When it comes to your next crown or veneer, the benefits of a digital restoration add up quickly.</h1>

  <div class="benefit benefit--sameday">A same-day<br>Restoration</div>
  <div class="benefit benefit--fit">A stronger,<br>more precise fit</div>
  <div class="benefit benefit--look">A beautiful,<br>natural appearance</div>
  <div class="benefit benefit--relax">A relaxing<br>Patient experience</div>

  <svg class="plus" style="top:1008px" viewBox="0 0 34 34"><path d="M14 2h6v12h12v6H20v12h-6V20H2v-6h12z" fill="#e2131a"/></svg>
  <svg class="plus" style="top:1097px" viewBox="0 0 34 34"><path d="M14 2h6v12h12v6H20v12h-6V20H2v-6h12z" fill="#e2131a"/></svg>
  <svg class="plus" style="top:1185px" viewBox="0 0 34 34"><path d="M14 2h6v12h12v6H20v12h-6V20H2v-6h12z" fill="#e2131a"/></svg>

  <div class="goodbye goodbye--crown">GOOD BYE<br>TEMPORARY<br>CROWN</div>
  <div class="goodbye goodbye--visit">GOOD BYE<br>SECOND VISIT.</div>
  <div class="goodbye goodbye--tray"><span>GOOD BYE<br>GOOEY TRAY</span></div>

  <div class="details">
    <p>Introducing crowns, veneers and bridges that happen in hours instead of days – no more temporaries, no more multiple visits, no messy dental impressions.</p>
    <p>Ask your dentist if a same-day restoration is right for you.</p>
  </div>

  <div class="contact-band">
    <span>48 W. Maple Rd. Brookfield, MI 48000</span><span>I</span><span>555.014.0372</span><span>I</span><span>info@oakridgedentalcare.com</span>
  </div>
</div>
</body>
</html>
```